Screening Mammography flyer for patients

We need a flyer design to inform our patients of our Screening Mammography program (it's a screening Diagnostic Imaging test). Women aged 50-74 years old are eligible for this exam. We also have a convenient booking system, when a patient can call us directly. There's no doctor’s referral needed to sign up for the test.
We are also starting the RVC Scan Champion program, when select patients will help spread the word and save lives.
The flyer has to be done with a lot of pink color as it is a traditional color for Breast cancer materials, with consideration of the hospital's corporate colors (the brand book is attached).

Industry/Entity Type

Diagnostic Imaging

```html
<!DOCTYPE html>
<html lang="en">
<head>
<meta charset="utf-8">
<title>Screening Mammography – Just Book It</title>
<link href="https://fonts.googleapis.com/css2?family=Exo+2:wght@700;800&family=Lato:wght@400;700&display=swap" rel="stylesheet">
<style>
  :root {
    --pink: #e8307f;
    --magenta: #d11f68;
    --headline: #c4125f;
    --ink: #222222;
    --body: #333333;
    --paper: #ffffff;
    --stage: #e6e6e6;
    --photo-light: #f7f2ec;
    --photo-mid: #b9b4b0;
    --badge-light: #fbd3e4;
    --badge-mid: #f294bd;
  }
  * { margin: 0; padding: 0; box-sizing: border-box; }
  html, body { width: 1200px; height: 1075px; overflow: hidden; background: var(--stage); }
  .flyer {
    position: absolute; left: 30px; top: 96px;
    width: 1362px; height: 1055px;
    transform: scale(0.837); transform-origin: top left;
    background: var(--paper); overflow: hidden;
    font-family: "Lato", sans-serif;
  }
  .flyer-shapes { position: absolute; inset: 0; }
  .headline {
    position: absolute; right: 49px; top: 66px;
    font-family: "Exo 2", sans-serif; font-weight: 800;
    font-size: 76px; color: var(--headline); letter-spacing: -1px; line-height: 1;
  }
  .audience {
    position: absolute; right: 49px; top: 158px;
    font-size: 58px; color: var(--ink); line-height: 1;
  }
  .referral-pill {
    position: absolute; left: 591px; top: 278px; width: 600px; height: 138px;
    background: var(--pink); border-radius: 42px;
    box-shadow: 0 18px 16px -12px rgba(0,0,0,0.25);
  }
  .referral-text {
    position: absolute; left: 600px; top: 305px; width: 480px;
    text-align: center; color: #fff; font-weight: 700; font-size: 28px; line-height: 42px;
  }
  .badge {
    position: absolute; left: 1113px; top: 232px; width: 226px; height: 226px;
    border-radius: 50%; background: #fff; border: 11px solid var(--pink);
  }
  .badge-placeholder {
    position: absolute; left: 1139px; top: 258px; width: 174px; height: 174px;
    border-radius: 50%;
    background: radial-gradient(circle at 40% 40%, var(--badge-light), var(--badge-mid));
  }
  .booking {
    position: absolute; left: 519px; top: 476px;
    color: var(--magenta); font-size: 38px; font-weight: 700; white-space: nowrap;
    letter-spacing: -0.3px;
  }
  .booking .call { color: var(--ink); font-size: 27px; font-weight: 700; }
  .same-day {
    position: absolute; right: 54px; top: 560px;
    font-family: "Exo 2", sans-serif; font-weight: 700;
    font-size: 47px; color: #fff; line-height: 68px;
  }
  .org-name {
    position: absolute; left: 406px; top: 712px;
    display: flex; align-items: center; gap: 14px;
    font-weight: 700; font-size: 24px; color: var(--magenta); line-height: 1.2;
  }
  .org-mark { width: 34px; height: 34px; background: var(--magenta); flex: none; }
  .contact-list { position: absolute; left: 748px; top: 676px; list-style: none; }
  .contact-list li {
    display: flex; align-items: flex-start; gap: 8px;
    font-size: 25px; color: var(--body); line-height: 30px; margin-bottom: 10px;
  }
  .contact-list svg { flex: none; margin-top: 5px; }
  .date-line {
    position: absolute; left: 421px; top: 850px;
    font-size: 35px; color: var(--ink); white-space: nowrap;
  }
</style>
</head>
<body>
<div class="flyer">
  <svg class="flyer-shapes" viewBox="0 0 1362 1055" width="1362" height="1055">
    <defs>
      <linearGradient id="photo-tone" x1="0" y1="0" x2="0" y2="1">
        <stop offset="0" stop-color="var(--photo-light)"/>
        <stop offset="0.45" stop-color="var(--photo-mid)"/>
        <stop offset="1" stop-color="#e9e6e3"/>
      </linearGradient>
    </defs>
    <path class="same-day-band" d="M330,554 H1362 V634 H330 Z" fill="var(--magenta)"/>
    <path role="img" aria-label="Photo of two smiling program ambassadors in grey t-shirts, with a decorative pink swirl"
          d="M0,0 H655 C520,200 420,520 300,660 C230,730 110,740 0,690 Z" fill="url(#photo-tone)"/>
    <path class="swoop" d="M655,0 H736 C600,190 480,520 370,640 C270,750 90,770 0,700 L0,688 C110,735 235,720 300,655 C420,520 520,200 655,0 Z" fill="var(--pink)"/>
    <path d="M0,850 Q681,1085 1362,862 V1055 H0 Z" fill="var(--pink)"/>
    <path d="M0,866 Q681,1105 1362,880 V1055 H0 Z" fill="var(--magenta)"/>
  </svg>

  <h1 class="headline">JUST BOOK IT</h1>
  <p class="audience">For women aged 50-74</p>

  <div class="referral-pill"></div>
  <p class="referral-text">No doctor's referral needed for<br>your screening Mammogram</p>

  <div class="badge"></div>
  <div class="badge-placeholder" role="img" aria-label="Awareness badge with pink ribbon about early detection"></div>

  <p class="booking">To book an appointment, <span class="call">call 555-014-2200 ext. 2100</span></p>
  <p class="same-day">Same Day appointments available!</p>

  <div class="org-name"><span class="org-mark"></span><span>Riverdale Valley Centre<br>RVC Scan Champion</span></div>

  <ul class="contact-list">
    <li><svg width="18" height="20" viewBox="0 0 18 20"><path d="M9 1a7 7 0 0 0-7 7c0 5 7 11 7 11s7-6 7-11a7 7 0 0 0-7-7z" fill="none" stroke="var(--pink)" stroke-width="2.2"/><circle cx="9" cy="8" r="2.5" fill="var(--pink)"/></svg><span>Diagnostic Imaging Department at Riverdale Valley<br>Centre, 120 Maple Grove Ave, Lakeside</span></li>
    <li><svg width="18" height="20" viewBox="0 0 18 20"><circle cx="9" cy="11" r="8" fill="var(--pink)"/><rect x="4.5" y="8" width="9" height="6" fill="none" stroke="#fff" stroke-width="1.3"/><path d="M4.5 8l4.5 3.5L13.5 8" fill="none" stroke="#fff" stroke-width="1.3"/></svg><span>imaging@rvcnetwork.ca</span></li>
    <li><svg width="18" height="20" viewBox="0 0 18 20"><circle cx="9" cy="11" r="8" fill="var(--pink)"/><circle cx="9" cy="11" r="5" fill="none" stroke="#fff" stroke-width="1.2"/><path d="M4 11h10M9 6v10" stroke="#fff" stroke-width="1.2"/></svg><span>www.rvcnetwork.ca/imaging</span></li>
  </ul>

  <p class="date-line">Date and Time: _________________________</p>
</div>
</body>
</html>
```